Post card design for ( Interior ) & ( Exterior ) Residential Painting

We need a post card design for interior painting. To get homeowners to call about getting there interior home painted before the end winter comes, to get a clean, quality and no hassle paint job with low odor paints

Some IDEAS:
Exterior Paint Season is Coming to Northern VA and Metro DC!
Have you taken a look around your house this winter? Have you noticed any areas of unwanted moisture, mold or draft? Keeping your house painted and well-maintained on the outside will save money in the future as well. It protects your home from the elements – whether, wind, rain and snow or the strong summer sun.

idea #2
Exterior Paint Makes Your House Last Longer
aintaining a good coat of the correct type of paint on the exterior of your home will help protect your home from the elements and extend the overall life of the structure
idea #3
Rotten Wood and Two Other TOP Reasons for Exterior Paint
We’ll start there – rotten wood – the first reason for exterior paint. If your home or building has decorative wood trim, wood siding or even wood around windows and doors, it could be at risk for rotten or rotting wood. Maintaining a healthy and COMPLETE coat of paint will protect the wood from water damage. Additionally, during a paint project, our team can assess wooden areas and advise if there are any places of concern. For a long-term solution, consider replacing wood trim with vinyl or wood alternatives that stand up to the elements. This can also be done during an exterior paint project.
Idea # 4
Benefits of Using Low-VOC interior Paints
Paints with low-VOC or Zero-VOC are considered healthier options due to the lower amount of toxins they release when applied to a wall. Latex paints are popular low-VOC because they are water based and don’t contain other chemicals you may find in oil-based paints.

Less odor! Because these paints have lower levels of toxins that are released, the paint smell that is associated with a fresh coat of paint is not as strong. Low-VOC would be a great option if you plan on painting a nursery because the smell won’t linger. Although you might not smell it, it is always important to ventilate the room. All paints, even low-VOC have levels of toxicity which are not good to breathe in for long periods of time.

Target Market(s)

single family homes

Colors

Designer to choose colors to be used in the design.

Requirements
Should not have
• cheep, free

```html
<!DOCTYPE html>
<html lang="en">
<head>
<meta charset="utf-8">
<title>Crestline Painting – Postcard</title>
<link rel="stylesheet" href="https://fonts.googleapis.com/css2?family=Oswald:wght@600&family=Merriweather:wght@300;700&family=Source+Sans+3:wght@600;700&display=swap">
<style>
  :root {
    --red: #e0193f;
    --ink: #231f20;
    --white: #ffffff;
    --stage: #c8c8c8;
    --display: "Oswald", sans-serif;
    --serif: "Merriweather", serif;
    --sans: "Source Sans 3", sans-serif;
  }
  * { box-sizing: border-box; margin: 0; padding: 0; }
  html, body { width: 1110px; height: 1200px; overflow: hidden; }
  body { background: var(--stage); position: relative; font-family: var(--sans); }
  .card {
    position: absolute; left: 54px; width: 1002px; height: 546px;
    background: var(--white); overflow: hidden;
    box-shadow: 6px 8px 12px rgba(0,0,0,.45);
  }
  .card--front { top: 38px; }
  .card--back { top: 616px; }
  .abs { position: absolute; }
  .art { position: absolute; left: 0; top: 0; width: 1002px; height: 546px; }

  .brand {
    font-family: var(--display); font-weight: 600; color: var(--ink);
    text-transform: uppercase; line-height: .98; display: flex; align-items: center; gap: 10px;
  }
  .brand__mark { width: 16px; height: 16px; background: var(--red); flex: none; }
  .brand--front { left: 22px; top: 32px; font-size: 36px; }
  .brand--back { left: 650px; top: 22px; font-size: 27px; }

  .headline {
    left: 232px; top: 30px; font-family: var(--display); font-weight: 600;
    font-size: 33px; line-height: 38px; color: var(--red); letter-spacing: -.3px;
  }
  .intro-band { left: 0; top: 150px; width: 522px; height: 150px; background: var(--ink); }
  .intro {
    left: 18px; top: 164px; width: 500px; font-family: var(--serif); font-weight: 300;
    font-size: 18px; line-height: 30.5px; color: var(--white);
  }
  .compare {
    top: 321px; height: 165px; display: flex; border: 2px solid var(--ink); background: var(--ink);
  }
  .compare--siding { left: 18px; width: 222px; }
  .compare--trim { left: 258px; width: 248px; }
  .compare__shot { flex: 1; height: 100%; }
  .compare__shot + .compare__shot { border-left: 2px solid var(--white); }
  .shot-white-wall { background: linear-gradient(160deg, #d7dadd, #9aa0a6 70%, #7b8a6c); }
  .shot-blue-wall { background: linear-gradient(160deg, #b6c6d4, #8ea2b6 60%, #6d7c66); }
  .shot-brick-old { background: linear-gradient(150deg, #5a6f8a 0%, #8a4a3a 35%, #6a3a2e 70%, #4b6a3a); }
  .shot-brick-new { background: linear-gradient(150deg, #7fb0e0 0%, #e8ecef 30%, #8a4a3a 55%, #5c7a3e); }
  .labels {
    top: 502px; left: 0; width: 520px; font-family: var(--sans); font-weight: 700;
    font-size: 19px; color: var(--white); letter-spacing: .3px;
  }
  .labels span { position: absolute; transform: translateX(-50%); }

  .badge { top: 402px; height: 56px; }
  .badge--rated { left: 612px; width: 80px; border: 2px solid #1f6b3a; border-top: 0; background: #f3f7f2; }
  .badge--accredited { left: 712px; width: 114px; height: 44px; border-radius: 6px; background: #1b6fa8; }
  .badge--guild { left: 832px; width: 76px; border: 2px solid #233f86; background: #fbeaea; }

  .contact { font-family: var(--sans); font-weight: 600; color: var(--white); display: flex; align-items: center; gap: 6px; white-space: nowrap; }
  .contact svg { width: 13px; height: 13px; fill: var(--red); flex: none; }
  .contact--gap { margin-left: 10px; }
  .front-contact { left: 556px; font-size: 18.5px; }

  .benefits-title {
    left: 18px; top: 16px; font-family: var(--serif); font-weight: 700; color: var(--white);
    text-transform: uppercase; letter-spacing: .3px;
  }
  .benefits-title__main { font-size: 38px; line-height: 46px; display: block; }
  .benefits-title__sub { font-size: 27px; line-height: 36px; display: block; }
  .benefits { left: 18px; top: 128px; width: 520px; list-style: none; }
  .benefits li {
    position: relative; padding-left: 37px; font-family: var(--sans); font-weight: 600;
    font-size: 14.2px; line-height: 18.4px; color: var(--white); margin-bottom: 11.5px;
  }
  .benefits li svg { position: absolute; left: 0; top: 2px; width: 31px; height: 28px; fill: var(--red); }
  .note {
    left: 18px; top: 340px; width: 470px; font-family: var(--serif); font-weight: 300;
    font-size: 14.4px; line-height: 18px; color: var(--white);
  }
  .call {
    right: 546px; top: 432px; font-family: var(--sans); font-weight: 600; font-size: 23px;
    color: var(--white); display: flex; align-items: center; gap: 7px;
  }
  .call svg { width: 17px; height: 17px; fill: var(--red); }
  .back-contact { left: 202px; font-size: 18.5px; }
  .back-contact svg { fill: var(--white); }
  .address {
    left: 620px; top: 101px; width: 190px; text-align: center; font-family: var(--sans);
    font-weight: 600; font-size: 14px; line-height: 18.5px; color: var(--ink);
  }
  .stamp { left: 880px; top: 20px; width: 99px; height: 112px; border: 2px solid var(--ink); }
</style>
</head>
<body>

<!-- Front: exterior -->
<section class="card card--front">
  <svg class="art" viewBox="0 0 1002 546" aria-hidden="true">
    <defs>
      <linearGradient id="houseTones" x1="0" y1="0" x2="0" y2="1">
        <stop offset="0" stop-color="#8fb4d6"/>
        <stop offset=".35" stop-color="#56607a"/>
        <stop offset=".75" stop-color="#4a5168"/>
        <stop offset="1" stop-color="#5f8a3a"/>
      </linearGradient>
    </defs>
    <g fill="none" stroke="var(--red)" stroke-width="4" stroke-linejoin="miter">
      <path d="M1002,390 L518,390 L518,252 L460,200 L668,8 L741,76 L741,28 L804,28 L804,122"/>
      <path d="M1002,380 L528,380 L528,246 L474,200 L668,20 L749,95 L749,36 L796,36 L796,122"/>
      <path d="M1002,370 L538,370 L538,240 L488,200 L668,32 L757,114 L757,44 L788,44 L788,122"/>
    </g>
    <polygon points="0,471 545,471 488,546 0,546" fill="var(--red)"/>
    <polygon points="560,471 1002,471 1002,512 760,512 747,546 503,546" fill="var(--ink)"/>
    <polygon points="760,512 1002,512 1002,546 747,546" fill="var(--red)"/>
  </svg>
  <svg class="art" viewBox="0 0 1002 546" role="img" aria-label="Photo of a freshly painted two-storey blue house with white trim and a stone base">
    <polygon points="558,354 558,190 668,62 780,150 780,122 1002,122 1002,354" fill="url(#houseTones)"/>
  </svg>

  <div class="abs brand brand--front"><span class="brand__mark"></span><span>Crestline<br>Painting</span></div>
  <h1 class="abs headline">EXTERIOR PAINT MAKES<br>YOUR HOUSE LAST LONGER</h1>

  <div class="abs intro-band"></div>
  <p class="abs intro">Maintaining a good coat of the correct type of paint on the exterior of your home will help protect your home from the elements and extend the overall life of the structure</p>

  <div class="abs compare compare--siding">
    <div class="compare__shot shot-white-wall" role="img" aria-label="Before: worn white siding"></div>
    <div class="compare__shot shot-blue-wall" role="img" aria-label="After: siding repainted blue"></div>
  </div>
  <div class="abs compare compare--trim">
    <div class="compare__shot shot-brick-old" role="img" aria-label="Before: faded shutters on a brick house"></div>
    <div class="compare__shot shot-brick-new" role="img" aria-label="After: bright blue shutters and white trim"></div>
  </div>
  <div class="abs labels">
    <span style="left:75px">BEFORE</span><span style="left:186px">AFTER</span>
    <span style="left:320px">BEFORE</span><span style="left:438px">AFTER</span>
  </div>

  <div class="abs badge badge--rated" role="img" aria-label="Rating badge"></div>
  <div class="abs badge badge--accredited" role="img" aria-label="Accreditation badge"></div>
  <div class="abs badge badge--guild" role="img" aria-label="Trade association badge"></div>

  <div class="abs contact front-contact" style="top:480px">
    <svg viewBox="0 0 24 24"><path d="M6.6 10.8a15.1 15.1 0 0 0 6.6 6.6l2.2-2.2a1 1 0 0 1 1-.25 11.4 11.4 0 0 0 3.6.57 1 1 0 0 1 1 1V20a1 1 0 0 1-1 1A17 17 0 0 1 3 4a1 1 0 0 1 1-1h3.5a1 1 0 0 1 1 1c0 1.25.2 2.45.57 3.57a1 1 0 0 1-.25 1z"/></svg>
    <span>555-014-2271</span>
    <svg class="contact--gap" viewBox="0 0 24 24"><path d="M2 5h20v14H2z M2 5l10 8 10-8" /></svg>
    <span>hello@crestlinepaint.com</span>
  </div>
  <div class="abs contact front-contact" style="top:508px">
    <svg viewBox="0 0 24 24"><circle cx="12" cy="12" r="10"/></svg>
    <span>crestlinepaint.com</span>
  </div>
</section>

<!-- Back: interior benefits + mailing side -->
<section class="card card--back">
  <svg class="art" viewBox="0 0 1002 546" aria-hidden="true">
    <polygon points="0,0 566,0 458,546 0,546" fill="var(--ink)"/>
    <polygon points="0,0 566,0 543,114 0,114" fill="var(--red)"/>
    <polygon points="574,0 584,0 476,546 466,546" fill="var(--red)"/>
    <polygon points="186,470 462,470 447,546 176,546" fill="var(--red)"/>
    <polygon points="0,440 194,440 180,546 0,546" fill="var(--white)"/>
  </svg>
  <svg class="art" viewBox="0 0 1002 546" role="img" aria-label="Photo of a warm living room with a fireplace">
    <defs>
      <linearGradient id="roomTones" x1="0" y1="0" x2="1" y2="1">
        <stop offset="0" stop-color="#e6c98a"/>
        <stop offset=".55" stop-color="#c59a5e"/>
        <stop offset="1" stop-color="#7e5a34"/>
      </linearGradient>
    </defs>
    <polygon points="0,446 188,446 175,546 0,546" fill="url(#roomTones)"/>
  </svg>

  <h2 class="abs benefits-title">
    <span class="benefits-title__main">Benefits of Using</span>
    <span class="benefits-title__sub">Low-VOC Interior Paints</span>
  </h2>

  <ul class="abs benefits">
    <li><svg viewBox="0 0 31 28"><path d="M15.5 1 1 14h4v13h8v-8h5v8h8V14h4z"/></svg>Paints with low-VOC or Zero-VOC are considered healthier options due to<br>the lower amount of toxins they release when applied to a wall.</li>
    <li><svg viewBox="0 0 31 28"><path d="M15.5 1 1 14h4v13h8v-8h5v8h8V14h4z"/></svg>Latex paints are popular low-VOC because they are water based and<br>don’t contain other chemicals you may find in oil-based paints.</li>
    <li><svg viewBox="0 0 31 28"><path d="M15.5 1 1 14h4v13h8v-8h5v8h8V14h4z"/></svg>Less odor! Because these paints have lower levels of toxins that are<br>released, the paint smell that is associated with a fresh coat of paint<br>is not as strong.</li>
    <li><svg viewBox="0 0 31 28"><path d="M15.5 1 1 14h4v13h8v-8h5v8h8V14h4z"/></svg>Low-VOC would be a great option if you plan on painting a nursery<br>because the smell won’t linger.</li>
  </ul>

  <p class="abs note">Although you might not smell it, it is always important to ventilate the room. All paints, even low-VOC have levels of toxicity which are not good to breathe in for long periods of time.</p>

  <div class="abs call">
    <span>Call us</span>
    <svg viewBox="0 0 24 24"><path d="M6.6 10.8a15.1 15.1 0 0 0 6.6 6.6l2.2-2.2a1 1 0 0 1 1-.25 11.4 11.4 0 0 0 3.6.57 1 1 0 0 1 1 1V20a1 1 0 0 1-1 1A17 17 0 0 1 3 4a1 1 0 0 1 1-1h3.5a1 1 0 0 1 1 1c0 1.25.2 2.45.57 3.57a1 1 0 0 1-.25 1z"/></svg>
    <span>555-014-2271</span>
  </div>
  <div class="abs contact back-contact" style="top:474px">
    <svg viewBox="0 0 24 24"><path d="M2 5h20v14H2z"/></svg>
    <span>hello@crestlinepaint.com</span>
  </div>
  <div class="abs contact back-contact" style="top:501px">
    <svg viewBox="0 0 24 24"><circle cx="12" cy="12" r="10"/></svg>
    <span>crestlinepaint.com</span>
  </div>

  <div class="abs brand brand--back"><span class="brand__mark"></span><span>Crestline<br>Painting</span></div>
  <p class="abs address">48 Maple Grove Lane, Suite 12, Fairview, Virginia 22000</p>
  <div class="abs stamp"></div>
</section>

</body>
</html>
```